Website Redesign for Accommodation Directory

We need a redesign for stayfinderhubzone.example
The new design needs to include a banner with overlaid text and a 'get started now' button. The overlaid text could be 'Find Hotels in Auckland, New Zealand' for example.
The new design needs to include:
- primary navigation in header
- an accommodation search (left or right column)
- a secondary navigation menu (under the search).
We will need the following font styles (including links for each) defined also please:
h1, h2, h3, h4, h5, h6, p, ul, ol, address, pre
Accommodation

```html
<!DOCTYPE html>
<html lang="en">
<head>
<meta charset="utf-8">
<title>Stay Finder Hub Zone – Accommodation Directory</title>
<link href="https://fonts.googleapis.com/css2?family=Arimo:wght@400;700&family=PT+Sans+Narrow:wght@400;700&family=Lato:wght@400;700&display=swap" rel="stylesheet">
<style>
:root{
  --red:#e3000f;
  --red-dark:#8a0008;
  --blue:#1b62b4;
  --blue-dark:#0d4d88;
  --navy:#173a66;
  --grey-text:#8a8a8a;
  --panel:#e6e6e6;
  --nav-top:#5b5b5b;
  --nav-bottom:#2f2f2f;
  --page-bg:#d3e1f1;
  --white:#ffffff;
}
*{box-sizing:border-box;margin:0;padding:0}
html,body{width:1200px;height:1181px;overflow:hidden}
body{background:var(--page-bg);font-family:"Arimo",Arial,sans-serif}
.stage{position:relative;width:1280px;height:1260px;transform:scale(.9375);transform-origin:0 0;
  background:linear-gradient(#eaf1f9 263px,#dbe6f3 700px,#c9daee 1260px)}
.red-band{position:absolute;left:0;top:0;width:1280px;height:263px;
  background:radial-gradient(ellipse at 50% 0,#f2121d 0,#d6000b 45%,#7d0006 100%)}
.abs{position:absolute}
.top-tabs a{position:absolute;top:16px;height:32px;background:var(--white);border-radius:4px 4px 0 0;
  color:var(--blue-dark);font-size:12px;text-decoration:none;text-align:center;line-height:32px}
.sheet{position:absolute;left:148px;top:46px;width:984px;height:1166px;background:var(--white);
  border:1px solid #c7ccd3;border-radius:8px;box-shadow:0 2px 6px rgba(0,0,0,.25)}
.brand{position:absolute;left:166px;top:66px;display:flex;align-items:center;gap:8px}
.brand-square{width:48px;height:48px;background:var(--red);border-radius:4px}
.brand-name{font-family:"Lato",sans-serif;font-size:38px;font-weight:700;color:#555;letter-spacing:-.5px}
.brand-url{position:absolute;left:224px;top:109px;font-size:10px;letter-spacing:6px;color:#777}
.btn-login{position:absolute;left:972px;top:80px;width:141px;height:36px;border-radius:4px;
  background:linear-gradient(#2a7bc6,#0c4a86);color:#fff;font-size:13px;line-height:36px;padding-left:12px;
  box-shadow:0 1px 2px rgba(0,0,0,.4)}
.btn-login svg{position:absolute;right:8px;top:11px}
.main-nav{position:absolute;left:161px;top:143px;width:959px;height:37px;border-radius:4px;
  background:linear-gradient(var(--nav-top),var(--nav-bottom));display:flex;align-items:center;padding-left:5px}
.main-nav a{color:#fff;text-decoration:none;font-size:14px;padding:0 13px;border-right:1px solid #555;line-height:20px}
.main-nav a:last-child{border:0}
.main-nav a.active{background:#1e1e1e;border-radius:3px;line-height:29px;padding:0 9px;margin-right:4px;border:0}
.banner-frame{position:absolute;left:160px;top:197px;width:960px;height:348px;border:1px solid #ddd;border-radius:4px;
  box-shadow:0 2px 4px rgba(0,0,0,.12)}
.banner-photo{position:absolute;left:170px;top:207px;width:940px;height:327px;
  background:linear-gradient(180deg,#9fb4cf 0,#c8cfd6 35%,#d8c8a8 60%,#9a8a70 100%)}
.banner-title{position:absolute;left:170px;top:230px;height:40px;padding:0 10px;background:rgba(255,255,255,.6);
  font-family:"PT Sans Narrow",sans-serif;font-weight:700;font-size:28px;color:#1d2a3a;line-height:40px;border-radius:0 20px 20px 0}
.btn-start{position:absolute;left:202px;top:460px;width:218px;height:52px;border-radius:4px;
  background:linear-gradient(#f56a3b,#d92a12);color:#fff;font-family:"PT Sans Narrow",sans-serif;font-size:23px;
  text-align:center;line-height:52px;box-shadow:0 2px 3px rgba(0,0,0,.4)}
.intro{position:absolute;left:160px;top:567px;width:683px;height:76px;background:var(--panel);border-radius:4px;
  color:var(--red);font-size:16.5px;line-height:20px;padding:6px 15px}
.copy{position:absolute;left:160px;top:658px;width:683px;color:var(--grey-text);font-size:12px;line-height:18px}
.copy p{margin-bottom:18px}
.copy a{color:var(--blue);font-weight:700;text-decoration:none}
.cta{position:absolute;left:160px;top:947px;width:683px;height:49px;background:linear-gradient(#f0f0f0,#e2e2e2);
  border:1px solid #d2d2d2;border-radius:4px;color:var(--blue);font-size:18px;text-align:center;line-height:47px}
.testimonials h3{position:absolute;left:160px;top:1028px;font-weight:400;font-size:17px;color:var(--navy)}
.testimonials .sub{position:absolute;left:160px;top:1050px;font-size:11px;color:#333}
.quote{position:absolute;left:161px;top:1072px;width:294px;height:103px;border:1px solid #d6d6d6;
  padding:16px 14px;font-size:11px;line-height:16px;color:#777}
.quote-name{position:absolute;left:476px;top:1079px;font-family:"PT Sans Narrow",sans-serif;font-weight:700;font-size:14px;color:#555}
.quote-role{position:absolute;left:476px;top:1095px;font-size:11px;color:#333}
.arrows{position:absolute;left:178px;top:1163px;display:flex;gap:6px}
.arrows span{width:24px;height:24px;border-radius:50%;border:1px solid #ccc;background:#f4f4f4;display:flex;align-items:center;justify-content:center}
.signup{position:absolute;left:544px;top:1025px;width:300px;height:158px;border-radius:5px;background:#aaa59c;
  box-shadow:inset 0 0 0 1px #9a958c}
.signup-label{position:absolute;left:645px;top:1043px;background:#fff;font-size:12px;padding:2px 5px;color:#111}
.signup-text{position:absolute;left:544px;top:1077px;width:300px;text-align:center;font-size:12px;line-height:18px;color:#222}
.signup-field{position:absolute;left:564px;top:1127px;width:222px;height:36px;background:linear-gradient(#e8e8e8,#fff);border-radius:4px 0 0 4px}
.signup-go{position:absolute;left:786px;top:1127px;width:38px;height:36px;background:var(--red);color:#fff;border-radius:0 4px 4px 0;
  font-size:18px;text-align:center;line-height:36px}
.search-box{position:absolute;left:862px;top:563px;width:259px;height:215px;border:1px solid #c9c9c9;border-radius:5px;
  background:linear-gradient(#fafafa,#ececec)}
.search-head{position:absolute;left:863px;top:564px;width:257px;height:60px;border-radius:4px 4px 0 0;
  background:linear-gradient(#e4101a,#b20009);color:#fff;font-size:18px;line-height:18px;padding:16px 0 0 78px}
.search-head svg{position:absolute;left:14px;top:12px}
.select{position:absolute;left:877px;width:228px;height:32px;border:1px solid #bbb;border-radius:3px;
  background:linear-gradient(#fafafa,#e3e3e3);font-size:12px;color:#333;line-height:30px;padding-left:13px}
.select i{position:absolute;right:0;top:0;width:29px;height:30px;border-left:1px solid #bbb;background:linear-gradient(#eee,#d4d4d4)}
.select i:after{content:"";position:absolute;left:10px;top:13px;border:4px solid transparent;border-top-color:#555}
.btn-search{position:absolute;left:948px;top:730px;width:82px;height:32px;border-radius:16px;
  background:linear-gradient(#5da9ea,#1f6fc2);color:#fff;font-size:16px;text-align:center;line-height:32px;border:1px solid #1d60a8}
.cats{position:absolute;left:863px;top:796px;width:257px;height:387px;border:1px solid #cfd8e2;border-radius:5px;
  background:linear-gradient(#dbe5f0,#eaf1f8)}
.cats h3{position:absolute;left:20px;top:8px;font-weight:400;font-size:18px;color:var(--red)}
.cats hr{position:absolute;left:0;top:38px;width:255px;border:0;border-top:1px solid #c5cfda}
.cats ul{position:absolute;left:20px;top:44px;width:218px;list-style:none}
.cats li{height:28px;border-bottom:1px dotted #aab;font-size:12px;color:#222;line-height:28px;padding-left:14px;position:relative}
.cats li:before{content:"";position:absolute;left:2px;top:10px;border:4px solid transparent;border-left-color:#888}
.cats li:last-child{border:0}
.footer{position:absolute;left:161px;top:1223px;font-size:11px;line-height:14px;color:var(--blue-dark)}
.social{position:absolute;top:1226px;width:16px;height:16px;border-radius:2px}
</style>
</head>
<body>
<div class="stage">
  <div class="red-band"></div>
  <nav class="top-tabs">
    <a style="left:669px;width:149px">Free Insurance Quotes</a>
    <a style="left:820px;width:149px">Free Website Statistics</a>
    <a style="left:971px;width:149px">Company Reviews</a>
  </nav>
  <div class="sheet"></div>

  <div class="brand"><span class="brand-square"></span><span class="brand-name">stayfinderhubzone</span></div>
  <div class="brand-url">www.stayfinderhubzone.example</div>
  <div class="btn-login">SUPPLIER LOGIN
    <svg width="14" height="14" viewBox="0 0 14 14"><path d="M7 2a5 5 0 1 0 5 5" fill="none" stroke="#fff" stroke-width="2"/><path d="M6 7h7M10 4l3 3-3 3" fill="none" stroke="#fff" stroke-width="2"/></svg>
  </div>
  <nav class="main-nav">
    <a class="active">HOME</a><a>ADD YOUR PROPERTY</a><a>SUPPLIER LOGIN</a><a>CONTACT US</a>
  </nav>

  <div class="banner-frame"></div>
  <div class="banner-photo" role="img" aria-label="Photo of white waterfront apartment hotels in Auckland under a blue sky"></div>
  <h1 class="banner-title">FIND HOTELS IN AUCKLAND, NEW ZEALAND</h1>
  <div class="btn-start">GET STARTED NOW</div>

  <div class="intro">You’ve come to the right place to find Accommodation in Any Country whether it’s a hotel, motel, backpackers, bed and breakfast or beach house you're after you'll find just what you need to enjoy your stay in Any Country.</div>
  <div class="copy">
    <p>With much to choose from you'll want to find a place that meets your needs. <a>Our accommodation search tool</a> will help you find the perfect place, regardless of what your price, location or style requirements might be.</p>
    <p>Our <a>Any Country accommodation directory</a> is perfect for times when you've scored cheap flights, desperately need last-minute accommodation or are just planning your next holiday or business trip to Any Country.</p>
    <p>With a great selection of Accommodation options in Any Country from cheap nights staying in budget accommodation to 5-star luxury Any Country hotels, so you can really treat yourself, you'll find it all here.</p>
    <p>Using this <a>Any Country Accommodation search tool</a> you'll quickly find a great place to stay offered by providers you can trust and depend on to make sure you get a good night's sleep. From well-known hotel chains to popular beach houses with rave reviews, it's easy to locate welcoming hospitality in Any Country.</p>
    <p>Avoid the hassle of running around Any Country, desperately hoping you'll find a vacancy and a place you won't regret staying at – just switch on to stayfinderhubzone.example to search, click and stay.</p>
  </div>
  <div class="cta">Ready to get started? Find Accommodation in Any Country online now.</div>

  <section class="testimonials">
    <h3>Testimonials</h3>
    <div class="sub">Lorem ipsum dolor</div>
    <div class="quote">Lorem ipsum dolor sit amet, consectetur adipisicing elit, sed do eiusmod tempor incididunt ut labore et dolore magna aliqua. Ut enim ad minim veniam, quis nostrud exercitation</div>
    <div class="quote-name">Jack</div>
    <div class="quote-role">Lorem ipsum</div>
    <div class="arrows">
      <span><svg width="8" height="8"><path d="M6 0L1 4l5 4z" fill="#999"/></svg></span>
      <span><svg width="8" height="8"><path d="M2 0l5 4-5 4z" fill="#999"/></svg></span>
    </div>
  </section>

  <div class="signup"></div>
  <div class="signup-label">EMAIL SIGN UP</div>
  <div class="signup-text">Sign up to our enewsletter to receive<br>news and updates.</div>
  <div class="signup-field"></div>
  <div class="signup-go">Go</div>

  <div class="search-box"></div>
  <div class="search-head">
    <svg width="60" height="40" viewBox="0 0 60 40"><circle cx="18" cy="18" r="15" fill="none" stroke="#3a0004" stroke-width="3"/><path d="M3 18h30M18 3v30M7 9h22M7 27h22" stroke="#3a0004" stroke-width="2"/><circle cx="32" cy="22" r="8" fill="none" stroke="#3a0004" stroke-width="3"/><path d="M38 28l9 9" stroke="#3a0004" stroke-width="4"/></svg>
    ACCOMMODATION<br>SEARCH
  </div>
  <div class="select" style="top:643px">All Countries<i></i></div>
  <div class="select" style="top:685px">All Categories<i></i></div>
  <div class="btn-search">Search</div>

  <aside class="cats">
    <h3>Categories</h3>
    <hr>
    <ul>
      <li>Apartments</li><li>Backpackers</li><li>Batch</li><li>Beach House</li><li>Bed And Breakfasts</li><li>Camping Sites</li>
      <li>Caravan Park</li><li>Holiday Homes</li><li>Hostels</li><li>Hotels</li><li>Lodges</li><li>Motels</li>
    </ul>
  </aside>

  <footer class="footer">© 2011 Stay Finder Hub Zone<br>Find Accommodation in Any Country - Accommodation Any Country | Recommend us | Contact Us | Sitemap</footer>
  <span class="social" style="left:1082px;background:#3b5b99"></span>
  <span class="social" style="left:1104px;background:#5fb7e6"></span>
</div>
</body>
</html>
```